Insurance Company Website Design

We are working with an insurance company. They sell home, auto, commercial, and health insurance. We like the "get a quote" in the banner of https://www.plovanta.example and https://www.quirelmog.example.

Some sites to use for content/competitors and inspiration:
https://velturbrookins.example
https://kamzubredainsurance.example
https://tvorpinsurance.example
https://www.insuranceforzelmarids.example
https://www.plovanta.example
https://www.quirelmog.example

Thank you for taking the time to consider designing a website for us. We are web developers based in Stockton, CA, USA. Most of our projects go through the same process. Understanding this process may help you win a project with us. We custom-code all of our websites in-house. We don’t have any requirements as to what tools you use for your design, but we ask that you follow these guidelines.

IMAGES:
If you use any images or icons in the design, we ask that you have a link to the asset so we can purchase the image/icon. Most of the designs we submit do not have the customer’s images on them unless they have some great images. Be creative; show us the feeling you are trying to portray with your image choices. Use any royalty-free site you choose. We subscribe to Quintrel and mainly use their images, but we can purchase images outside of Quintrel. PLEASE NOTE: we will not submit designs to clients with watermarks on the images.

FONTS:
We ask that you identify the fonts you’re using in the design. This can be done in a message if you want. We typically use Google Fonts and Quintrel Fonts.

CONTENT:
We're always open to different content and ideas. We often submit designs with stock images so the client can see our vision. We typically take pictures after the website launch to use their images with our vision. Lorem Ipsum is fine for paragraphs, but we ask that you make the Headers with correct English. We want to be able to show the vision and identify the sections of the website.

INSPIRATION:
We typically add a couple of links in the brief of websites we like to help you get started in your design.

REVISIONS:
We do not often ask for revisions of the designs unless we see something in the design that may not appeal to the client. If there are slight changes that we want to make, we do that in the development process.

FEEDBACK:
We rarely give feedback on designs during the design process. We are working on many website projects and do not have the time to provide feedback. We usually respond if your request is well thought out and asks specific questions, but a note asking “feedback, please” usually goes unanswered.

```html
<!DOCTYPE html>
<html lang="en">
<head>
<meta charset="utf-8">
<title>Covenly Insurance</title>
<link href="https://fonts.googleapis.com/css2?family=Gelasio:wght@400;700&family=Nunito+Sans:wght@400;600;700;800&display=swap" rel="stylesheet">
<style>
:root{
  --navy:#1f3a6e;
  --navy-deep:#17284d;
  --teal:#00a8cc;
  --lav:#f1eff8;
  --lav-2:#e4e1f1;
  --ink:#2b2f3a;
  --dark:#262b36;
  --grey:#8a8d99;
  --white:#fff;
  --star:#f07b1d;
  --brand:#1d6fc4;
}
*{box-sizing:border-box;margin:0;padding:0}
html,body{width:1200px;height:4562px;overflow:hidden}
body{position:relative;background:var(--white);font-family:"Nunito Sans",sans-serif;color:var(--ink)}
.abs{position:absolute}
.serif{font-family:"Gelasio",serif}
.btn{position:absolute;display:flex;align-items:center;justify-content:center;font-weight:700;border-radius:22px;font-size:14px}

/* header */
.top-info{position:absolute;top:18px;display:flex;gap:12px;align-items:center;font-size:11px;line-height:14px}
.top-info .ico{width:28px;height:28px;border-radius:50%;background:var(--teal);display:flex;align-items:center;justify-content:center}
.top-info b{display:block;font-weight:700}
.top-info span{color:var(--grey)}
.nav-rule{position:absolute;top:70px;height:1px;background:#d9dbe3}
.nav a{position:absolute;top:84px;font-size:12px;color:var(--ink);text-decoration:none}
.brand{position:absolute;font-family:"Nunito Sans",sans-serif;font-weight:600;color:var(--brand)}
.appt{top:12px;left:880px;width:182px;height:39px;background:var(--navy);color:#fff;font-size:11px;text-transform:uppercase}

/* hero */
.hero-kicker{left:88px;top:324px;color:#fff;font-size:14px;letter-spacing:3px;font-weight:700}
.hero-title{left:86px;top:356px;color:#fff;font-size:45px;font-weight:800;line-height:58px}
.hero-rule{left:88px;top:493px;width:632px;height:1px;background:rgba(255,255,255,.7)}
.hero-copy{left:90px;top:524px;width:620px;color:#fff;font-size:15px;font-weight:700;line-height:26px}

/* about */
.kicker{font-family:"Gelasio",serif;color:var(--navy);font-size:16px}
.h2{font-family:"Gelasio",serif;color:var(--navy);font-weight:400}
.muted{color:var(--grey);font-size:13px;line-height:23px}

/* services */
.svc{position:absolute;top:1788px;width:319px;height:265px;border-radius:6px;overflow:hidden}
.svc h3{position:absolute;left:26px;top:62px;font-family:"Gelasio",serif;color:#fff;font-size:24px;font-weight:700}
.svc-ico{position:absolute;top:1752px;width:72px;height:72px;border-radius:50%;background:#fff;box-shadow:0 4px 14px rgba(0,0,0,.12);display:flex;align-items:center;justify-content:center}

/* why */
.feat{position:absolute;width:260px}
.feat h4{font-family:"Gelasio",serif;color:var(--navy);font-weight:400;font-size:20px;margin-bottom:10px}
.feat p{color:var(--grey);font-size:13px;line-height:23px}
.feat.left{text-align:right}
.why-ico{position:absolute;width:88px;height:88px;border-radius:50%;background:var(--navy);border:6px solid #fff;box-shadow:0 3px 12px rgba(31,58,110,.3);display:flex;align-items:center;justify-content:center}

/* contact */
.hours{position:absolute;left:97px;top:3053px;width:491px;height:234px;background:rgba(20,24,34,.82);border-left:4px solid var(--teal);padding:0 36px}
.hours .row{display:flex;justify-content:space-between;height:51px;align-items:center;color:#fff;font-size:15px;border-bottom:1px solid rgba(255,255,255,.18)}
.hours .row:last-child{border-bottom:none}
.hours .row b{font-weight:700}
.form{position:absolute;left:612px;top:2883px;width:491px;height:499px;background:var(--lav)}
.field{position:absolute;height:51px;background:#fff;border:1px solid #e6e4ef;color:var(--grey);font-size:14px;padding-left:26px;display:flex;align-items:center}

/* reviews */
.rev{position:absolute;top:3694px;width:320px;height:266px;background:#fff;box-shadow:0 6px 20px rgba(31,58,110,.1);padding:68px 28px 0}
.rev .av{position:absolute;left:28px;top:-30px;width:62px;height:62px;border-radius:50%;background:linear-gradient(160deg,#d6d4dc,#8d8a96);border:3px solid #fff;box-shadow:0 2px 8px rgba(0,0,0,.12)}
.rev .q{position:absolute;right:30px;top:-20px;font-family:"Gelasio",serif;font-size:110px;line-height:90px;color:#9fdcee;font-weight:700}
.rev .stars{color:var(--star);font-size:16px;letter-spacing:3px}
.rev p{color:var(--grey);font-size:13px;line-height:23px;margin-top:12px}
.rev h5{font-family:"Gelasio",serif;color:var(--navy);font-weight:400;font-size:18px;margin-top:14px}
.rev small{display:block;font-size:10px;color:var(--ink);margin-top:6px;letter-spacing:.5px}

/* footer */
.fnav a{position:absolute;top:4322px;color:#fff;font-size:14px;font-weight:700;text-decoration:none}
.fitem{position:absolute;top:4419px;display:flex;align-items:center;gap:18px;color:#fff;font-size:11px;font-weight:700;line-height:17px}
.fitem .ring{width:56px;height:56px;border-radius:50%;border:2px solid rgba(255,255,255,.8);display:flex;align-items:center;justify-content:center}
.fitem .big{font-size:14px}
.soc{position:absolute;top:4522px;width:24px;height:24px;border:1.5px solid #fff;border-radius:3px}
</style>
</head>
<body>

<!-- HEADER -->
<header>
  <div class="top-info" style="left:124px">
    <div class="ico"><svg width="14" height="14" viewBox="0 0 24 24" fill="#fff"><path d="M6.6 10.8a15 15 0 0 0 6.6 6.6l2.2-2.2c.3-.3.7-.4 1-.2 1.1.4 2.3.6 3.6.6.6 0 1 .4 1 1V20c0 .6-.4 1-1 1A17 17 0 0 1 3 4c0-.6.4-1 1-1h3.5c.6 0 1 .4 1 1 0 1.3.2 2.5.6 3.6.1.3 0 .7-.2 1z"/></svg></div>
    <div><b>Call Us:</b><span>(555) 010-4432</span></div>
  </div>
  <div class="top-info" style="left:282px">
    <div class="ico"><svg width="14" height="14" viewBox="0 0 24 24" fill="#fff"><path d="M3 6h18v12H3zm2 2v.5l7 4.5 7-4.5V8l-7 4.5z"/></svg></div>
    <div><b>Email:</b><span>office@company.com</span></div>
  </div>
  <div class="nav-rule" style="left:124px;width:359px"></div>
  <div class="nav-rule" style="left:696px;width:370px"></div>
  <nav class="nav">
    <a style="left:132px">Home</a>
    <a style="left:244px">About Us</a>
    <a style="left:394px">Services</a>
    <a style="left:713px">Our Team</a>
    <a style="left:841px">Gallery</a>
    <a style="left:965px">Contact Us</a>
  </nav>
  <div class="brand" style="left:483px;width:213px;text-align:center;top:48px;font-size:42px;line-height:48px">Covenly</div>
  <div class="btn appt">Make Appointment</div>
</header>

<!-- HERO -->
<section>
  <svg class="abs" style="left:0;top:124px" width="1200" height="780" viewBox="0 0 1200 780">
    <defs>
      <linearGradient id="heroG" x1="0" y1="0" x2="1" y2="1">
        <stop offset="0" stop-color="#2f4f78"/>
        <stop offset=".55" stop-color="#243e63"/>
        <stop offset="1" stop-color="#5b7497"/>
      </linearGradient>
    </defs>
    <path role="img" aria-label="Business team meeting around a conference table, blue tinted photo" d="M0 0H1200V655Q600 845 0 655Z" fill="url(#heroG)"/>
    <path d="M238 734Q602 790 965 734" fill="none" stroke="var(--teal)" stroke-width="5"/>
    <path d="M238 730Q602 785 965 730" fill="none" stroke="var(--navy)" stroke-width="2"/>
  </svg>
  <div class="abs" style="left:572px;top:860px;width:60px;height:60px;border-radius:50%;background:#fff;box-shadow:0 3px 10px rgba(0,0,0,.12);display:flex;align-items:center;justify-content:center"><div style="width:14px;height:14px;border-radius:50%;background:var(--teal)"></div></div>
  <div class="abs hero-kicker">INSURANCE SERVICES</div>
  <h1 class="abs hero-title">Insure Your Future, Secure<br>Your Dreams</h1>
  <div class="abs hero-rule"></div>
  <p class="abs hero-copy">Lorem ipsum dolor sit amet, consectetur adipiscing elit et dolore conser tempor incididunt ut labore et dolore magna</p>
  <div class="btn" style="left:83px;top:612px;width:145px;height:39px;background:var(--teal);color:#fff;font-size:13px">LEARN MORE</div>
  <div class="btn" style="left:239px;top:612px;width:181px;height:39px;background:#fff;color:var(--ink);font-size:14px;font-weight:600">REQUEST QUOTE</div>
</section>

<!-- ABOUT -->
<section>
  <svg class="abs" style="left:80px;top:990px" width="480" height="480" viewBox="0 0 480 480">
    <path d="M240 5A235 235 0 1 1 5 240" fill="none" stroke="#4f6b96" stroke-width="6"/>
    <path d="M5 240A235 235 0 0 1 240 5" fill="none" stroke="#4f6b96" stroke-width="2"/>
    <circle role="img" aria-label="Two colleagues reviewing a laptop together" cx="240" cy="240" r="215" fill="#c3c7cf"/>
  </svg>
  <div class="abs kicker" style="left:620px;top:1014px">About Us</div>
  <h2 class="abs h2" style="left:620px;top:1046px;font-size:42px;line-height:54px">Insurance Excellence,<br>Your Assurance</h2>
  <div class="abs" style="left:621px;top:1168px;height:59px;border-left:3px solid var(--navy);padding-left:16px;width:470px">
    <p class="muted" style="font-size:13px;line-height:22px">Lorem ipsum dolor sit amet, consectetur adipiscing elit, sed do eiusmod or incididunt ut labore et dolore</p>
  </div>
  <p class="abs muted" style="left:620px;top:1252px;width:470px">Lorem ipsum dolor sit amet, consectetur adipiscing elit, sed do eiusmod tem por incididunt ut labore et dolore magna aliqua. Ut enim ad minim veniam, quis nostrud exercitation ullamco laboris nisi ut aliquip ex ea commodo consequat. Duis aute irure dolor in reprehenderit in voluptate velit esse cillum dolore eu fugiat nulla pariatur. Excepteur</p>
  <div class="btn" style="left:620px;top:1398px;width:153px;height:46px;border-radius:3px;background:var(--teal);color:#fff;font-size:15px;gap:10px">Learn More <svg width="18" height="14" viewBox="0 0 18 14"><path d="M1 7h15M10 1l6 6-6 6" stroke="#fff" stroke-width="2" fill="none"/></svg></div>
</section>

<!-- SERVICES -->
<section>
  <div class="abs" style="left:0;top:1549px;width:1200px;height:571px;background:var(--lav)"></div>
  <h2 class="abs h2" style="left:0;width:1200px;text-align:center;top:1610px;font-size:44px">Our Services</h2>
  <p class="abs muted" style="left:0;width:1200px;text-align:center;top:1677px">Lorem ipsum dolor sit amet, consectetur adipiscing elit, sed do eiusmod temp<br>or incididunt ut labore et dolore</p>
  <div class="svc" style="left:92px" role="img" aria-label="Driver looking out of a car window"><div style="position:absolute;inset:0;background:linear-gradient(160deg,#5d6c5a,#c9cdd2)"></div><h3>Auto Insurance</h3></div>
  <div class="svc" style="left:439px" role="img" aria-label="Hand sheltering a small model house"><div style="position:absolute;inset:0;background:linear-gradient(170deg,#8c8fa0,#cfd6e6 60%,#2d4d8a)"></div><h3>Home Insurance</h3></div>
  <div class="svc" style="left:786px" role="img" aria-label="Senior man receiving care at home"><div style="position:absolute;inset:0;background:linear-gradient(160deg,#2c3b5c,#9ea2ad)"></div><h3>Health Insurance</h3></div>
  <div class="svc-ico" style="left:134px"><svg width="30" height="30" viewBox="0 0 30 30" fill="none" stroke="var(--teal)" stroke-width="2.2"><path d="M4 26V18M10 26V13M16 26V16M22 26V8M4 12l7-6 5 4 8-7"/></svg></div>
  <div class="svc-ico" style="left:483px"><svg width="30" height="30" viewBox="0 0 30 30" fill="none" stroke="var(--teal)" stroke-width="2"><circle cx="15" cy="15" r="5"/><circle cx="15" cy="15" r="10" stroke-dasharray="2 3"/></svg></div>
  <div class="svc-ico" style="left:830px"><svg width="30" height="30" viewBox="0 0 30 30" fill="none" stroke="var(--teal)" stroke-width="2"><path d="M12 16V6a3 3 0 0 1 6 0v10M9 18c0 5 3 9 6 9s6-4 6-9"/></svg></div>
</section>

<!-- WHY CHOOSE US -->
<section>
  <h2 class="abs h2" style="left:0;width:1200px;text-align:center;top:2175px;font-size:44px">Why Choose Us</h2>
  <p class="abs muted" style="left:0;width:1200px;text-align:center;top:2240px">Lorem ipsum dolor sit amet, consectetur adipiscing elit, sed do eiusmod temp<br>or incididunt ut labore et dolore</p>
  <svg class="abs" style="left:0;top:2340px" width="1200" height="460" viewBox="0 0 1200 460">
    <defs>
      <linearGradient id="blobL" x1="1" y1="0" x2="0" y2="0"><stop offset="0" stop-color="#e7e4f3"/><stop offset="1" stop-color="#fff" stop-opacity="0"/></linearGradient>
      <linearGradient id="blobR" x1="0" y1="0" x2="1" y2="0"><stop offset="0" stop-color="#e7e4f3"/><stop offset="1" stop-color="#fff" stop-opacity="0"/></linearGradient>
    </defs>
    <circle cx="441" cy="226" r="216" fill="url(#blobL)"/>
    <circle cx="759" cy="226" r="216" fill="url(#blobR)"/>
    <circle role="img" aria-label="Smiling businessman with arms crossed" cx="589" cy="209" r="190" fill="#4a5e86"/>
  </svg>
  <div class="feat left" style="left:115px;top:2397px"><h4>Professional</h4><p>Lorem ipsum dolor sit amet, consectet ur adipiscing elit et dolore conser</p></div>
  <div class="feat left" style="left:115px;top:2528px"><h4>Empathetic Staff</h4><p>Lorem ipsum dolor sit amet, consectet ur adipiscing elit et dolore conser</p></div>
  <div class="feat left" style="left:115px;top:2661px"><h4>Personal Approach</h4><p>Lorem ipsum dolor sit amet, consectet ur adipiscing elit et dolore conser</p></div>
  <div class="feat" style="left:797px;top:2397px"><h4>Experienced Experts</h4><p>Lorem ipsum dolor sit amet, consectet ur adipiscing elit et dolore conser</p></div>
  <div class="feat" style="left:797px;top:2528px"><h4>Proven Track Record</h4><p>Lorem ipsum dolor sit amet, consectet ur adipiscing elit et dolore conser</p></div>
  <div class="feat" style="left:797px;top:2661px"><h4>Quality Services</h4><p>Lorem ipsum dolor sit amet, consectet ur adipiscing elit et dolore conser</p></div>
  <div class="why-ico" style="left:397px;top:2395px"><svg width="32" height="32" viewBox="0 0 32 32" fill="none" stroke="#fff" stroke-width="2.2"><circle cx="16" cy="6" r="2.5"/><path d="M6 12h20M16 12v8l-6 9M16 20l6 9"/></svg></div>
  <div class="why-ico" style="left:397px;top:2526px"><svg width="32" height="32" viewBox="0 0 32 32" stroke="#fff" stroke-width="2.5" stroke-linecap="round"><path d="M16 4v5M16 23v5M4 16h5M23 16h5M7.5 7.5l3.5 3.5M21 21l3.5 3.5M7.5 24.5L11 21M21 11l3.5-3.5"/></svg></div>
  <div class="why-ico" style="left:397px;top:2659px"><svg width="32" height="32" viewBox="0 0 32 32" fill="none" stroke="#fff" stroke-width="2.2"><path d="M8 18a8 8 0 1 1 16 0M6 18h20v4H6zM16 22v5"/></svg></div>
  <div class="why-ico" style="left:692px;top:2395px"><svg width="32" height="32" viewBox="0 0 32 32" fill="none" stroke="#fff" stroke-width="2"><circle cx="16" cy="16" r="12"/><circle cx="16" cy="16" r="7"/><circle cx="16" cy="16" r="2.5" fill="#fff"/></svg></div>
  <div class="why-ico" style="left:692px;top:2526px"><svg width="32" height="32" viewBox="0 0 32 32" fill="none" stroke="#fff" stroke-width="2.2"><path d="M7 17a9 9 0 0 1 18 0v7H7zM11 20h10"/></svg></div>
  <div class="why-ico" style="left:692px;top:2659px"><svg width="32" height="32" viewBox="0 0 32 32" fill="none" stroke="#fff" stroke-width="2.2"><rect x="5" y="5" width="7" height="7"/><rect x="20" y="5" width="7" height="7"/><rect x="5" y="20" width="7" height="7"/><rect x="20" y="20" width="7" height="7"/><path d="M12 8.5h8M8.5 12v8M23.5 12v8"/></svg></div>
</section>

<!-- CONTACT -->
<section>
  <div class="abs" role="img" aria-label="Dark office background with a world map overlay" style="left:0;top:2857px;width:1200px;height:559px;background:linear-gradient(100deg,#1e232e,#353b48 55%,#262b36)"></div>
  <h3 class="abs serif" style="left:94px;top:2990px;color:#fff;font-size:26px;font-weight:400">Open Hours</h3>
  <div class="hours">
    <div class="row"><b>Monday - Friday</b><span>08am - 05pm</span></div>
    <div class="row"><b>Saturday</b><span>08am - 05pm</span></div>
    <div class="row"><b>Telephone</b><span>+123 456 7890</span></div>
    <div class="row"><b>Email</b><span>info@company.com</span></div>
  </div>
  <div class="form">
    <div class="abs" style="left:52px;top:38px;width:56px;height:56px;border-radius:50%;background:#4b5a85;display:flex;align-items:center;justify-content:center"><svg width="26" height="26" viewBox="0 0 26 26" fill="none" stroke="#fff" stroke-width="1.8"><rect x="3" y="7" width="20" height="14"/><path d="M3 8l10 7 10-7"/></svg></div>
    <div class="abs serif" style="left:130px;top:46px;font-size:30px;color:var(--navy)">Get in touch with us</div>
  </div>
  <div class="field" style="left:667px;top:3020px;width:183px">First Name</div>
  <div class="field" style="left:869px;top:3020px;width:182px">Last Name</div>
  <div class="field" style="left:667px;top:3090px;width:183px">Email Address</div>
  <div class="field" style="left:869px;top:3090px;width:182px">Phone Number</div>
  <div class="field" style="left:667px;top:3161px;width:384px">Select Subject</div>
  <div class="field" style="left:667px;top:3232px;width:384px">dd/mm/yyyy</div>
  <div class="btn" style="left:667px;top:3308px;width:384px;height:50px;border-radius:0;background:var(--teal);color:#fff;font-size:18px;font-weight:800">SUBMIT</div>
</section>

<!-- REVIEWS -->
<section>
  <div class="abs" style="left:0;top:3416px;width:1200px;height:720px;background:var(--lav)"></div>
  <h2 class="abs h2" style="left:0;width:1200px;text-align:center;top:3498px;font-size:44px">Clients Reviews</h2>
  <p class="abs muted" style="left:0;width:1200px;text-align:center;top:3560px">Lorem ipsum dolor sit amet, consectetur adipiscing elit, sed do eiusmod temp<br>or incididunt ut labore et dolore</p>
  <div class="rev" style="left:101px"><div class="av" role="img" aria-label="Client portrait"></div><div class="q">”</div><div class="stars">★★★★★</div><p>Lorem ipsum dolor sit amet, consectetur adipiscing elit, sed do eiusmod tempor inci didunt ut labore et dolore magna aliqua. Ut enim ad minim veniam, quis</p><h5>Mira Holvane</h5><small>BUSINESSMAN</small></div>
  <div class="rev" style="left:446px;border-bottom:5px solid var(--navy)"><div class="av" role="img" aria-label="Client portrait"></div><div class="q" style="color:var(--teal)">”</div><div class="stars">★★★★★</div><p>Lorem ipsum dolor sit amet, consectetur adipiscing elit, sed do eiusmod tempor inci didunt ut labore et dolore magna aliqua. Ut enim ad minim veniam, quis</p><h5>Mira Holvane</h5><small>BUSINESSMAN</small></div>
  <div class="rev" style="left:789px"><div class="av" role="img" aria-label="Client portrait"></div><div class="q">”</div><div class="stars">★★★★★</div><p>Lorem ipsum dolor sit amet, consectetur adipiscing elit, sed do eiusmod tempor inci didunt ut labore et dolore magna aliqua. Ut enim ad minim veniam, quis</p><h5>Mira Holvane</h5><small>BUSINESSMAN</small></div>
</section>

<!-- FOOTER -->
<footer>
  <svg class="abs" style="left:0;top:4030px" width="1200" height="480" viewBox="0 0 1200 480">
    <path d="M0 8Q600 150 1200 8V480H0Z" fill="var(--dark)"/>
    <path d="M238 55Q602 90 965 55" fill="none" stroke="var(--teal)" stroke-width="5"/>
    <path d="M238 51Q602 85 965 51" fill="none" stroke="var(--navy)" stroke-width="2"/>
  </svg>
  <div class="abs" style="left:572px;top:4085px;width:60px;height:60px;border-radius:50%;background:#fff;display:flex;align-items:center;justify-content:center"><div style="width:14px;height:14px;border-radius:50%;background:var(--teal)"></div></div>
  <div class="brand" style="left:0;width:1200px;text-align:center;top:4224px;font-size:44px;line-height:50px">Covenly</div>
  <nav class="fnav">
    <a style="left:357px">HOME</a>
    <a style="left:451px">SERVICES</a>
    <a style="left:556px">ABOUT US</a>
    <a style="left:675px">TESTIMONIALS</a>
    <a style="left:827px">BLOG</a>
  </nav>
  <div class="abs" style="left:142px;top:4374px;width:916px;height:1px;background:rgba(255,255,255,.55)"></div>
  <div class="abs" style="left:430px;top:4410px;width:2px;height:64px;background:rgba(255,255,255,.7)"></div>
  <div class="abs" style="left:750px;top:4410px;width:2px;height:64px;background:rgba(255,255,255,.7)"></div>
  <div class="fitem" style="left:172px"><div class="ring"><svg width="28" height="28" viewBox="0 0 28 28" fill="none" stroke="#fff" stroke-width="1.6"><circle cx="14" cy="14" r="11"/><path d="M3 14h22M14 3c4 4 4 18 0 22M14 3c-4 4-4 18 0 22"/></svg></div><div>123, Building Name, Street<br>City, State XY 123456</div></div>
  <div class="fitem" style="left:507px"><div class="ring"><svg width="24" height="28" viewBox="0 0 24 28" fill="none" stroke="#fff" stroke-width="1.6"><rect x="6" y="3" width="12" height="22" rx="2"/><path d="M10 21h4"/></svg></div><div><span class="big">PHONE</span><br>(123) 456 7890</div></div>
  <div class="fitem" style="left:827px"><div class="ring"><svg width="28" height="28" viewBox="0 0 28 28" fill="none" stroke="#fff" stroke-width="1.6"><rect x="4" y="8" width="20" height="14"/><path d="M4 9l10 7 10-7"/></svg></div><div><span class="big">EMAIL</span><br>info@company.com</div></div>
  <div class="abs" style="left:0;top:4505px;width:1200px;height:57px;background:#2b3a67"></div>
  <div class="abs" style="left:154px;top:4526px;color:#fff;font-size:13px;font-weight:700">Covenly</div>
  <div class="soc" style="left:934px"></div>
  <div class="soc" style="left:966px"></div>
  <div class="soc" style="left:998px"></div>
  <div class="soc" style="left:1030px"></div>
</footer>

</body>
</html>
```